Business cards and logo for a international shipping company called Meridane Freight LLC. We would like to incorporate the colors red and blue. We would like the theme to be nautical.

Industry/Entity Type

Business

```html
<!DOCTYPE html>
<html lang="en">
<head>
<meta charset="utf-8">
<title>Meridane Freight LLC — Business Cards</title>
<link rel="stylesheet" href="https://fonts.googleapis.com/css2?family=Questrial&display=swap">
<style>
  :root {
    --navy: #1d1a4f;
    --navy-soft: #262263;
    --ink: #1d1a4f;
    --sea-blue: #1f7ac4;
    --signal-red: #c8252c;
    --paper: #ffffff;
    --canvas: #ffffff;
  }
  * { margin: 0; padding: 0; box-sizing: border-box; }
  html, body {
    width: 1200px; height: 1185px; overflow: hidden;
    background: var(--canvas);
    font-family: "Questrial", "Helvetica Neue", Arial, sans-serif;
  }
  .sheet {
    position: relative; width: 1200px; height: 1185px;
    display: flex; align-items: center; justify-content: center; gap: 40px;
  }
  .card {
    position: relative; width: 540px; height: 314px; overflow: hidden;
    box-shadow: 0 6px 14px rgba(0,0,0,0.28);
  }

  /* Front */
  .card--front { background: var(--navy); }
  .card__pattern {
    position: absolute; inset: 0;
    background: radial-gradient(circle at 50% 45%, var(--navy-soft), var(--navy) 75%);
  }
  .hull-stripe {
    position: absolute; left: 0; right: 0; height: 4px; background: var(--signal-red);
  }
  .hull-stripe--low { bottom: 22px; }
  .hull-stripe--thin { bottom: 32px; height: 2px; background: var(--paper); opacity: 0.85; }
  .front-brand {
    position: absolute; left: 0; right: 0; top: 104px;
    display: flex; flex-direction: column; align-items: center; gap: 18px;
  }
  .brand-dot { width: 44px; height: 44px; border-radius: 50%; flex: none; }
  .front-brand .brand-dot { background: var(--signal-red); }
  .front-brand__name {
    color: var(--paper); font-size: 23px; letter-spacing: 0.2px;
    text-transform: uppercase; white-space: nowrap;
  }

  /* Back */
  .card--back { background: var(--paper); }
  .band {
    position: absolute; left: 0; right: 0;
    background: linear-gradient(90deg, var(--navy), var(--navy-soft) 50%, var(--navy));
  }
  .band--top { top: 0; height: 30px; }
  .band--bottom { bottom: 0; height: 46px; }
  .band-rule { position: absolute; left: 0; right: 0; height: 3px; background: var(--signal-red); }
  .band-rule--top { top: 30px; }
  .band-rule--bottom { bottom: 46px; }
  .back-brand {
    position: absolute; left: 0; right: 0; top: 62px;
    display: flex; align-items: center; justify-content: center; gap: 14px;
  }
  .back-brand .brand-dot { width: 46px; height: 46px; background: var(--sea-blue); }
  .back-brand__name {
    display: flex; flex-direction: column;
    color: var(--ink); text-transform: uppercase; white-space: nowrap;
  }
  .back-brand__line1 { font-size: 28px; line-height: 28px; letter-spacing: -0.3px; }
  .back-brand__line2 { font-size: 18px; line-height: 22px; letter-spacing: -0.2px; }
  .holder {
    position: absolute; left: 36px; top: 170px;
    color: var(--sea-blue); font-size: 18px; white-space: nowrap;
  }
  .divider {
    position: absolute; left: 280px; top: 176px; width: 2px; height: 64px;
    background: var(--ink);
  }
  .contact {
    position: absolute; left: 306px; top: 174px;
    list-style: none; color: var(--ink); font-size: 13.5px; line-height: 17px;
  }
  .contact__item { display: flex; align-items: flex-start; gap: 12px; margin-bottom: 9px; }
  .contact__icon { width: 17px; height: 17px; flex: none; }
</style>
</head>
<body>
<main class="sheet">
  <section class="card card--front" aria-label="Business card front">
    <div class="card__pattern" role="img" aria-label="Subtle repeating nautical pattern of anchors and ship wheels in dark navy"></div>
    <span class="hull-stripe hull-stripe--thin"></span>
    <span class="hull-stripe hull-stripe--low"></span>
    <div class="front-brand">
      <span class="brand-dot"></span>
      <span class="front-brand__name">Meridane Freight LLC</span>
    </div>
  </section>

  <section class="card card--back" aria-label="Business card back">
    <div class="band band--top" role="img" aria-label="Navy band with nautical pattern of anchors and ship wheels"></div>
    <span class="band-rule band-rule--top"></span>
    <div class="back-brand">
      <span class="brand-dot"></span>
      <span class="back-brand__name">
        <span class="back-brand__line1">Meridane</span>
        <span class="back-brand__line2">Freight, LLC</span>
      </span>
    </div>
    <p class="holder">Halvard Brennsholm</p>
    <span class="divider"></span>
    <ul class="contact">
      <li class="contact__item">
        <svg class="contact__icon" viewBox="0 0 20 20" aria-hidden="true">
          <circle cx="10" cy="10" r="10" fill="var(--ink)"/>
          <path d="M5 9.5c0-2 2.2-3.2 5-3.2s5 1.2 5 3.2l-2 .6-.6-1.6H7.6L7 10.1z" fill="#fff"/>
          <rect x="7" y="10.5" width="6" height="3.5" rx="0.8" fill="#fff"/>
        </svg>
        <span>(203) 555-0148</span>
      </li>
      <li class="contact__item">
        <svg class="contact__icon" viewBox="0 0 20 20" aria-hidden="true">
          <circle cx="10" cy="10" r="10" fill="var(--ink)"/>
          <path d="M10 4.5a3.6 3.6 0 0 1 3.6 3.6c0 2.6-3.6 6.6-3.6 6.6S6.4 10.7 6.4 8.1A3.6 3.6 0 0 1 10 4.5z" fill="#fff"/>
          <circle cx="10" cy="8.1" r="1.4" fill="var(--ink)"/>
        </svg>
        <span>418 Tidewater Lane<br>Marlow Bay, CT 06830</span>
      </li>
    </ul>
    <span class="band-rule band-rule--bottom"></span>
    <div class="band band--bottom" role="img" aria-label="Navy band with nautical pattern of anchors and ship wheels"></div>
  </section>
</main>
</body>
</html>
```